Creative & Professional Business Card for hair salon

We are looking to update our business cards. Our salon is creative, modern, progressive and professional and looking for a design that will reflect this.

```html
<!DOCTYPE html>
<html lang="en">
<head>
<meta charset="utf-8">
<title>Skyline Hair Studio – Business Card</title>
<link rel="stylesheet" href="https://fonts.googleapis.com/css2?family=Arimo:wght@400;700&display=swap">
<style>
  :root {
    --bg: #e9e7e4;
    --card-front: #ffffff;
    --card-back: #17181a;
    --brand-blue: #4f7f9c;
    --brand-light: #7fb0c6;
    --band-dark: #4a7895;
    --band-light: #a9cfdc;
    --ink: #2f3236;
    --silver: #d6d8da;
    --rule: #6c97ae;
  }
  * { box-sizing: border-box; margin: 0; padding: 0; }
  html, body { width: 1200px; height: 769px; overflow: hidden; }
  body {
    background: var(--bg);
    font-family: "Arimo", Arial, sans-serif;
    position: relative;
  }
  .card {
    position: absolute;
    width: 525px;
    height: 300px;
    top: 235px;
    border-radius: 3px;
    overflow: hidden;
    box-shadow: 0 6px 18px rgba(0,0,0,.18);
  }
  .card--front { left: 50px; background: var(--card-front); }
  .card--back { left: 625px; background: var(--card-back); }

  .brand {
    position: absolute;
    left: 80px;
    top: 46px;
    display: flex;
    align-items: center;
    gap: 12px;
  }
  .brand__dot {
    width: 34px; height: 34px;
    border-radius: 50%;
    background: var(--brand-light);
  }
  .brand__name {
    font-size: 33px;
    font-weight: 400;
    color: var(--brand-blue);
    letter-spacing: .3px;
  }
  .rule-top {
    position: absolute;
    left: 170px; top: 100px;
    width: 330px; height: 1px;
    background: var(--rule);
  }
  .contact {
    position: absolute;
    right: 28px; top: 110px;
    list-style: none;
    text-align: right;
    font-size: 12.5px;
    line-height: 17px;
    color: var(--ink);
  }
  .contact li { display: flex; justify-content: flex-end; align-items: center; gap: 7px; }
  .contact svg { width: 11px; height: 11px; flex: none; }

  .rule-name {
    position: absolute;
    left: 24px; top: 182px;
    width: 300px; height: 1px;
    background: var(--rule);
  }
  .person { position: absolute; left: 30px; top: 190px; }
  .person__name { font-size: 21px; font-weight: 700; color: var(--brand-blue); line-height: 23px; }
  .person__role { font-size: 15px; color: var(--brand-light); line-height: 18px; }
  .person__address { font-size: 13px; color: var(--ink); line-height: 16px; margin-top: 2px; }

  .band { position: absolute; left: 0; bottom: 0; width: 525px; height: 40px; }

  .back-brand {
    position: absolute;
    inset: 0;
    display: flex; align-items: center; justify-content: center;
    gap: 14px;
  }
  .back-brand__dot { width: 40px; height: 40px; border-radius: 50%; background: var(--silver); }
  .back-brand__name { font-size: 36px; font-weight: 400; color: var(--silver); }
</style>
</head>
<body>

<section class="card card--front" aria-label="Business card front">
  <div class="brand">
    <span class="brand__dot"></span>
    <span class="brand__name">Skyline Hair Studio</span>
  </div>
  <div class="rule-top"></div>

  <ul class="contact">
    <li>07 5310 4827
      <svg viewBox="0 0 12 12"><path fill="#5f8eaa" d="M3 1l2 2.3-1.1 1.2a6 6 0 0 0 3.6 3.6L8.7 7 11 9l-1.3 1.8C5.6 11 1 6.4 1.2 2.3z"/></svg>
    </li>
    <li>hello@skylinehair.com.ac
      <svg viewBox="0 0 12 12"><rect x="1" y="2.5" width="10" height="7" fill="#5f8eaa"/><path d="M1 2.5l5 4 5-4" stroke="#fff" fill="none" stroke-width="1"/></svg>
    </li>
    <li>SkylineHairByAvaReed
      <svg viewBox="0 0 12 12"><circle cx="6" cy="6" r="5.5" fill="#5f8eaa"/></svg>
    </li>
    <li>www.skylinehair.com.ac
      <svg viewBox="0 0 12 12"><circle cx="6" cy="6" r="5" fill="none" stroke="#5f8eaa" stroke-width="1.3"/><path d="M1 6h10M6 1c-2.5 3-2.5 7 0 10M6 1c2.5 3 2.5 7 0 10" stroke="#5f8eaa" fill="none" stroke-width=".9"/></svg>
    </li>
  </ul>

  <div class="rule-name"></div>
  <div class="person">
    <p class="person__name">Alex Morgan</p>
    <p class="person__role">CEO/Founder</p>
    <p class="person__address">5/21 Harbour Lane<br>Maleny</p>
  </div>

  <svg class="band" viewBox="0 0 525 40" preserveAspectRatio="none" aria-hidden="true">
    <defs>
      <linearGradient id="bandFill" x1="0" x2="1" y1="0" y2="0">
        <stop offset="0" stop-color="var(--band-light)"/>
        <stop offset=".55" stop-color="var(--band-dark)"/>
        <stop offset="1" stop-color="var(--band-dark)"/>
      </linearGradient>
    </defs>
    <polyline points="0,24 300,24 316,12 525,12" fill="none" stroke="var(--band-dark)" stroke-width="1"/>
    <polygon points="0,31 306,31 322,18 525,18 525,40 0,40" fill="url(#bandFill)"/>
  </svg>
</section>

<section class="card card--back" aria-label="Business card back">
  <div class="back-brand">
    <span class="back-brand__dot"></span>
    <span class="back-brand__name">Skyline Hair Studio</span>
  </div>
</section>

</body>
</html>
```